Tallow Microsystems PowerPoint Master Slide Deck Design

This is a 2-phase project to design a slide deck for a semiconductor company in the Silicon Valley. The design budget will be increased with each phase.
The slide deck will need to have one version with a dark background for presentations and a second version with a white background. Otherwise, the slides will be the same. I anticipate we will need a total of 10 slides, but that number may change.
The first phase will be to design a Title and a Title and Content slide.
- The Title Slide is the first slide of the deck. It should include the presentation title, the presenter's name and date of presentation
- The Title and Content slide should include a title and content with bullet points and up to 2 additional sub-bullets
- The Title and Content slide should have a footer that includes the slide #, Tallow Microsystems Confidential, and the logo. This footer will be on every slide except the Title Slide
The first two slides will serve as the format for the remaining ~8 slides:
-Header and Content Text (1, 2, 4 column)
-Header and Content Image (bar chart, pie chart, tables)
-Break
-Title only
-Closing (Tallow logo only)
Our slides contain a lot of content so a clean and simple design is best.
Both phases will need to include pre-set color options for
-Text and Lines
-Shadows
-Bullets and sub-bullets (including shapes, ex. circle, slash, square, etc.)
-Bar charts, pie charts, tables
Samples of our collateral are attached. Logo files are also attached
Look and feel
Each slider illustrates characteristics of the customer's brand and the style your logo design should communicate.

```html
<!DOCTYPE html>
<html lang="en">
<head>
<meta charset="utf-8">
<title>Tallow Microsystems Slide Master</title>
<link href="https://fonts.googleapis.com/css2?family=Poppins:wght@400;500;600;700&display=swap" rel="stylesheet">
<style>
:root{
  --blue:#0b52aa;
  --blue-mid:#1565c8;
  --blue-pale:#dde7f5;
  --blue-wash:#eef3fa;
  --ink:#151515;
  --grey:#6a6a6a;
  --orange:#e9531d;
  --paper:#ffffff;
  --canvas:#ffffff;
}
*{margin:0;padding:0;box-sizing:border-box}
html,body{width:1200px;height:3953px;overflow:hidden;background:var(--canvas);font-family:'Poppins',sans-serif;color:var(--ink)}
.slide{position:absolute;left:77px;width:1047px;height:590px;background:var(--paper);overflow:hidden;box-shadow:0 2px 10px rgba(0,0,0,.12)}
.deco{position:absolute;left:0;top:0;width:1047px;height:590px}
.motif{position:absolute}
.date{position:absolute;right:24px;top:32px;font-size:14px;font-weight:600}
.foot-note{position:absolute;left:37px;top:532px;font-size:14px;font-weight:600}
.foot-page{position:absolute;right:18px;top:532px;font-size:14px;font-weight:500}
.foot-brand{position:absolute;left:450px;top:528px;display:flex;align-items:center;gap:6px;font-size:15px;font-weight:600;color:var(--blue)}
.foot-brand i,.brand i{display:block;border-radius:50%;background:var(--blue)}
.foot-brand i{width:12px;height:12px}
.accent{position:absolute;width:52px;height:3px;background:var(--blue)}
.heading{position:absolute;font-size:34px;font-weight:600;white-space:nowrap}
.heading span{color:var(--blue)}
.brand{position:absolute;display:flex;align-items:center;justify-content:center;gap:12px;font-weight:600;color:var(--blue)}
/* title */
.title-main{position:absolute;left:0;width:1047px;top:255px;text-align:center;font-size:40px;font-weight:700}
.title-main span{color:var(--blue)}
.title-sub{position:absolute;left:0;width:1047px;top:325px;text-align:center;font-size:16px;font-weight:500}
.title-name{position:absolute;left:0;width:1047px;top:405px;text-align:center;font-size:17px;font-weight:600}
.title-name span{color:var(--blue)}
/* about */
.photo{position:absolute;background:linear-gradient(135deg,#0b2f7a,#3a8ae0 50%,#0a2560)}
.about-body{position:absolute;left:479px;top:185px;width:540px;font-size:10.5px;line-height:18px;font-weight:500;text-align:justify}
.bullets{position:absolute;left:479px;top:300px;width:540px;list-style:none}
.bullets li{position:relative;padding-left:30px;font-size:10.5px;font-weight:500;margin-bottom:8px}
.bullets li::before{content:"";position:absolute;left:2px;top:3px;width:12px;height:12px;border-radius:50%;border:2px solid var(--blue);box-shadow:inset 0 0 0 2px #fff;background:var(--blue)}
.bullets li.sub{font-size:10px;color:var(--grey);line-height:18px;margin-bottom:14px;font-weight:400;padding-left:45px}
.bullets li.sub::before{content:"→";border:0;background:none;box-shadow:none;width:auto;height:auto;top:-1px;left:30px;color:var(--blue);font-size:11px}
/* infograph */
.info-label{position:absolute;width:180px;text-align:center;font-size:12px;line-height:21px;color:#444}
/* overview */
.stats-card{position:absolute;left:111px;top:213px;width:856px;height:198px;background:#fff;border-radius:14px;box-shadow:0 4px 18px rgba(0,0,0,.1)}
.stat{position:absolute;top:40px}
.stat-num{font-size:36px;font-weight:700;color:var(--orange);line-height:44px;margin-top:6px}
.stat-label{font-size:13px;font-weight:600;color:var(--blue)}
.portrait{position:absolute;border-radius:50%;background:linear-gradient(160deg,#cfd6df,#7d8b9b)}
/* team */
.member{position:absolute;top:150px;width:216px;height:340px;background:#fff;border-radius:10px;box-shadow:0 3px 14px rgba(0,0,0,.1);overflow:hidden}
.member-band{position:absolute;left:0;top:0;width:216px;height:125px;background:var(--blue)}
.member .portrait{left:34px;top:20px;width:148px;height:148px;border:5px solid #fff}
.member-name{position:absolute;top:182px;width:100%;text-align:center;font-size:15px;font-weight:600;color:var(--blue)}
.member-role{position:absolute;top:208px;width:100%;text-align:center;font-size:12px;color:#555}
.member-rule{position:absolute;left:93px;top:235px;width:30px;height:2px;background:var(--blue)}
.member ul{position:absolute;left:22px;top:255px;list-style:none}
.member li{font-size:10px;line-height:21px;padding-left:18px;position:relative}
.member li::before{content:"";position:absolute;left:0;top:8px;width:6px;height:6px;border-radius:50%;background:var(--blue)}
</style>
</head>
<body>

<!-- Slide: Title -->
<section class="slide" style="top:72px">
  <svg class="deco" viewBox="0 0 1047 590">
    <circle cx="55" cy="-55" r="240" fill="var(--blue-pale)"/>
    <circle cx="45" cy="-70" r="240" fill="var(--blue)"/>
  </svg>
  <div class="motif" role="img" aria-label="Decorative circuit-node graphic" style="left:560px;top:90px;width:487px;height:500px;background:linear-gradient(200deg,rgba(221,231,245,0) 20%,var(--blue-pale) 70%,rgba(11,82,170,.35));clip-path:polygon(100% 0,100% 100%,0 100%)"></div>
  <div class="date">December 13,2023</div>
  <div class="brand" style="left:0;width:1047px;top:120px;font-size:34px"><i style="width:30px;height:30px"></i>Tallow Microsystems</div>
  <h1 class="title-main"><span>Presentation</span> Title Goes Here</h1>
  <p class="title-sub">Credential Subtitle Presentation</p>
  <p class="title-name">Mara <span>Linden</span></p>
  <div class="foot-note" style="top:538px">Tallow Microsystems Confidential</div>
</section>

<!-- Slide: About -->
<section class="slide" style="top:715px">
  <div class="motif" role="img" aria-label="Faint circuit-node decoration" style="left:0;top:0;width:1047px;height:300px;background:linear-gradient(165deg,rgba(238,243,250,0) 35%,var(--blue-wash) 55%,rgba(238,243,250,0) 75%)"></div>
  <div class="date">December 13,2023</div>
  <div class="photo" role="img" aria-label="Close-up of a glowing microchip on a circuit board" style="left:28px;top:89px;width:377px;height:362px"></div>
  <div class="accent" style="left:479px;top:97px"></div>
  <h2 class="heading" style="left:479px;top:115px">About <span>Us</span></h2>
  <p class="about-body">Lorem ipsum dolor sit amet, consectetur adipiscing elit, sed do eiusmod tempor incididunt ut labore et dolore magna aliqua. Ut enim ad minim veniam, quis nostrud exercitation ullamco laboris nisi ut aliquip ex ea commodo consequat. Duis aute irure dolor in reprehenderit in voluptate velit esse cillum dolore eu fugiat nulla pariatur. Excepteur sint occaecat cupidatat non proident, sunt in culpa qui officia deserunt mollit anim id est laborum.</p>
  <ul class="bullets">
    <li>Lorem ipsum dolor sit amet, consectetur adipiscing elit, sed do eiusmod tempor</li>
    <li class="sub">Sed ut perspiciatis unde omnis iste natus error sit voluptatem accusantium doloremque laudantium, totam rem aperiam, eaque ipsa quae.</li>
    <li>Lorem ipsum dolor sit amet, consectetur adipiscing elit, sed do eiusmod tempor</li>
    <li class="sub">Sed ut perspiciatis unde omnis iste natus error sit voluptatem accusantium doloremque laudantium, totam rem aperiam, eaque ipsa quae.</li>
  </ul>
  <div class="foot-note">Tallow Microsystems Confidential</div>
  <div class="foot-brand"><i></i>Tallow</div>
  <div class="foot-page">Page 1</div>
</section>

<!-- Slide: Infograph -->
<section class="slide" style="top:1357px">
  <svg class="deco" viewBox="0 0 1047 590">
    <polyline points="100,259 219,348 342,259 461,348 584,259 703,348 829,259 947,348" stroke="var(--blue)" stroke-width="14" fill="none"/>
    <g fill="#fff" stroke="var(--blue)" stroke-width="2">
      <circle cx="100" cy="259" r="55"/><circle cx="342" cy="259" r="55"/><circle cx="584" cy="259" r="55"/><circle cx="829" cy="259" r="55"/>
      <circle cx="219" cy="348" r="55"/><circle cx="461" cy="348" r="55"/><circle cx="703" cy="348" r="55"/><circle cx="947" cy="348" r="55"/>
    </g>
    <g fill="#fff" stroke="var(--blue-pale)" stroke-width="5">
      <circle cx="100" cy="259" r="46"/><circle cx="342" cy="259" r="46"/><circle cx="584" cy="259" r="46"/><circle cx="829" cy="259" r="46"/>
      <circle cx="219" cy="348" r="46"/><circle cx="461" cy="348" r="46"/><circle cx="703" cy="348" r="46"/><circle cx="947" cy="348" r="46"/>
    </g>
    <g fill="none" stroke="var(--blue)" stroke-width="1.5">
      <rect x="86" y="245" width="28" height="28" rx="3"/><text x="100" y="263" font-size="9" text-anchor="middle" fill="var(--blue)" stroke="none" font-family="Poppins,sans-serif">CPU</text>
      <rect x="326" y="248" width="34" height="24"/><rect x="338" y="253" width="14" height="12"/>
      <rect x="570" y="244" width="28" height="30"/><rect x="578" y="252" width="12" height="12"/>
      <circle cx="829" cy="259" r="14"/><rect x="824" y="253" width="10" height="12"/>
      <rect x="209" y="338" width="20" height="20"/><circle cx="219" cy="348" r="4"/>
      <rect x="451" y="334" width="20" height="28" rx="2"/><line x1="455" y1="341" x2="467" y2="341"/>
      <circle cx="703" cy="348" r="12"/><circle cx="703" cy="348" r="4"/>
      <rect x="937" y="336" width="20" height="24" rx="2"/><polyline points="949,340 943,349 951,349 945,357"/>
    </g>
  </svg>
  <div class="date">December 13,2023</div>
  <div class="accent" style="left:497px;top:40px"></div>
  <h2 class="heading" style="left:0;width:1047px;text-align:center;top:55px">Our <span>Infograph</span></h2>
  <p class="info-label" style="left:10px;top:140px">Lorem ipsum dolor sit<br>amet, consectetur</p>
  <p class="info-label" style="left:252px;top:140px">Lorem ipsum dolor sit<br>amet, consectetur</p>
  <p class="info-label" style="left:494px;top:140px">Lorem ipsum dolor sit<br>amet, consectetur</p>
  <p class="info-label" style="left:739px;top:140px">Lorem ipsum dolor sit<br>amet, consectetur</p>
  <p class="info-label" style="left:129px;top:412px">Lorem ipsum dolor sit<br>amet, consectetur</p>
  <p class="info-label" style="left:371px;top:412px">Lorem ipsum dolor sit<br>amet, consectetur</p>
  <p class="info-label" style="left:613px;top:412px">Lorem ipsum dolor sit<br>amet, consectetur</p>
  <p class="info-label" style="left:857px;top:412px">Lorem ipsum dolor sit<br>amet, consectetur</p>
  <div class="foot-note">Tallow Microsystems Confidential</div>
  <div class="foot-brand"><i></i>Tallow</div>
  <div class="foot-page">Page 2</div>
</section>

<!-- Slide: Company overview -->
<section class="slide" style="top:1999px">
  <svg class="deco" viewBox="0 0 1047 590">
    <circle cx="1010" cy="227" r="138" fill="var(--blue)"/>
  </svg>
  <div class="motif" role="img" aria-label="Decorative circuit-node graphic" style="left:0;top:0;width:360px;height:430px;background:linear-gradient(125deg,var(--blue-pale),rgba(11,82,170,.3) 45%,rgba(221,231,245,0) 80%);clip-path:polygon(0 0,100% 0,0 100%)"></div>
  <div class="date">December 13,2023</div>
  <div class="accent" style="left:525px;top:95px"></div>
  <h2 class="heading" style="left:525px;top:112px">Company <span>Overview</span></h2>
  <div class="stats-card">
    <div class="portrait" role="img" aria-label="Engineer inspecting a wafer in a lab" style="left:30px;top:22px;width:148px;height:148px;border:4px solid #fff;box-shadow:0 0 0 2px var(--blue)"></div>
    <div class="stat" style="left:224px">
      <svg width="30" height="30" viewBox="0 0 30 30" fill="none" stroke="var(--blue)" stroke-width="1.5"><circle cx="15" cy="10" r="7"/><path d="M4 26 q11-10 22 0"/></svg>
      <div class="stat-num">12k</div><div class="stat-label">Lorum Ipsum</div></div>
    <div class="stat" style="left:382px">
      <svg width="30" height="30" viewBox="0 0 30 30" fill="none" stroke="var(--blue)" stroke-width="1.5"><circle cx="15" cy="15" r="12"/><circle cx="15" cy="15" r="5"/></svg>
      <div class="stat-num">20k</div><div class="stat-label">Lorum Ipsum</div></div>
    <div class="stat" style="left:540px">
      <svg width="30" height="30" viewBox="0 0 30 30" fill="none" stroke="var(--blue)" stroke-width="1.5"><rect x="7" y="4" width="16" height="12" rx="2"/><path d="M3 26 l6-8 M27 26 l-6-8"/></svg>
      <div class="stat-num">12k</div><div class="stat-label">Lorum Ipsum</div></div>
    <div class="stat" style="left:699px">
      <svg width="30" height="30" viewBox="0 0 30 30" fill="none" stroke="var(--blue)" stroke-width="1.5"><circle cx="15" cy="15" r="12"/><path d="M9 18 q6 6 12 0"/></svg>
      <div class="stat-num">12k</div><div class="stat-label">Customer Satisfy</div></div>
  </div>
  <div class="foot-note">Tallow Microsystems Confidential</div>
  <div class="foot-brand"><i></i>Tallow</div>
  <div class="foot-page">Page 3</div>
</section>

<!-- Slide: Team -->
<section class="slide" style="top:2642px">
  <div class="motif" role="img" aria-label="Faint circuit-node decoration" style="left:0;top:0;width:300px;height:330px;background:linear-gradient(135deg,var(--blue-wash),rgba(238,243,250,0) 70%)"></div>
  <div class="date">December 13,2023</div>
  <div class="accent" style="left:497px;top:40px"></div>
  <h2 class="heading" style="left:0;width:1047px;text-align:center;top:58px">Team <span>Members</span></h2>
  <article class="member" style="left:46px"><div class="member-band"></div><div class="portrait" role="img" aria-label="Portrait of team member in a suit"></div><h3 class="member-name">Elio Varga</h3><p class="member-role">Manager of Lorum</p><div class="member-rule"></div><ul><li>Lorem ipsumsit ametconsec</li><li>Lorem ipsumsit ametconsec</li><li>Lorem ipsumsit ametconsec</li></ul></article>
  <article class="member" style="left:292px"><div class="member-band"></div><div class="portrait" role="img" aria-label="Portrait of team member in a suit"></div><h3 class="member-name">Elio Varga</h3><p class="member-role">Manager of Lorum</p><div class="member-rule"></div><ul><li>Lorem ipsumsit ametconsec</li><li>Lorem ipsumsit ametconsec</li><li>Lorem ipsumsit ametconsec</li></ul></article>
  <article class="member" style="left:537px"><div class="member-band"></div><div class="portrait" role="img" aria-label="Portrait of team member in a suit"></div><h3 class="member-name">Elio Varga</h3><p class="member-role">Manager of Lorum</p><div class="member-rule"></div><ul><li>Lorem ipsumsit ametconsec</li><li>Lorem ipsumsit ametconsec</li><li>Lorem ipsumsit ametconsec</li></ul></article>
  <article class="member" style="left:783px"><div class="member-band"></div><div class="portrait" role="img" aria-label="Portrait of team member in a suit"></div><h3 class="member-name">Elio Varga</h3><p class="member-role">Manager of Lorum</p><div class="member-rule"></div><ul><li>Lorem ipsumsit ametconsec</li><li>Lorem ipsumsit ametconsec</li><li>Lorem ipsumsit ametconsec</li></ul></article>
  <div class="foot-note">Tallow Microsystems Confidential</div>
  <div class="foot-brand" style="left:440px"><i></i>Tallow</div>
  <div class="foot-page" style="right:28px">Page 4</div>
</section>

<!-- Slide: Closing -->
<section class="slide" style="top:3285px">
  <svg class="deco" viewBox="0 0 1047 590">
    <circle cx="741" cy="0" r="137" fill="var(--blue)"/>
    <line x1="560" y1="387" x2="700" y2="387" stroke="var(--blue-mid)" stroke-width="1"/>
    <line x1="770" y1="387" x2="910" y2="387" stroke="var(--blue-mid)" stroke-width="1"/>
    <circle cx="735" cy="387" r="6" fill="none" stroke="var(--blue)" stroke-width="1.5"/>
  </svg>
  <div class="motif" role="img" aria-label="Decorative circuit-node graphic" style="left:0;top:0;width:680px;height:590px;background:linear-gradient(60deg,rgba(11,82,170,.3),var(--blue-pale) 35%,rgba(221,231,245,0) 65%);clip-path:polygon(0 0,35% 0,100% 100%,0 100%)"></div>
  <div class="date">December 13,2023</div>
  <div class="brand" style="left:535px;top:255px;width:400px;font-size:44px"><i style="width:28px;height:28px"></i>Tallow</div>
  <div class="brand" style="left:535px;top:318px;width:400px;font-size:24px">Microsystems</div>
  <div class="foot-note" style="top:540px">Tallow Microsystems Confidential</div>
</section>

</body>
</html>
```